R & T Summit Construction Business Card ideas

We want a business card to represents our company in a way that looks professional but is also a business card that is unique!

Industry/Entity Type

Construction Company

Contact Information for Business Card

open to all design ideas, just want to be able to see different options to choose from in either color or grayscale.

Requirements
Must have
• Our names and phone numbers
• Nolan Pritchett 512-804-2271
• Curtis Hale 512-693-1804
• Business logo

```html
<!DOCTYPE html>
<html lang="en">
<head>
<meta charset="utf-8">
<title>R &amp; T Summit Construction – Business Card</title>
<link href="https://fonts.googleapis.com/css2?family=Lato:wght@400;700&display=swap" rel="stylesheet">
<style>
  :root {
    --backdrop: #474747;
    --card-light: #f2f2f2;
    --card-dark: #000000;
    --ink: #111111;
    --ink-reverse: #ffffff;
  }
  * { margin: 0; padding: 0; box-sizing: border-box; }
  html, body {
    width: 1200px; height: 900px; overflow: hidden;
    background: var(--backdrop);
    font-family: "Lato", sans-serif;
  }
  .stage { position: relative; width: 1200px; height: 900px; }
  .card { position: absolute; top: 200px; width: 310px; height: 502px; }
  .card-front {
    left: 265px; background: var(--card-light); color: var(--ink);
    border-radius: 55px 0 55px 0;
  }
  .card-back {
    left: 641px; width: 309px; background: var(--card-dark); color: var(--ink-reverse);
    border-radius: 0 55px 0 55px;
  }
  .company-name {
    position: absolute; font-weight: 700; line-height: 1.1; letter-spacing: 0.3px;
  }
  .card-front .company-name { left: 30px; top: 62px; width: 250px; font-size: 25px; }
  .card-back .company-name { left: 59px; top: 384px; width: 200px; font-size: 20px; }
  .contact { position: absolute; left: 28px; }
  .contact-first { top: 256px; }
  .contact-second { top: 343px; }
  .contact-name { font-size: 18.5px; font-weight: 700; margin-bottom: 4px; }
  .contact-line {
    display: flex; align-items: center; gap: 7px;
    font-size: 13.5px; line-height: 19px;
  }
  .contact-line svg { width: 9px; height: 9px; flex: none; fill: var(--ink); }
</style>
</head>
<body>
<div class="stage">
  <section class="card card-front">
    <div class="company-name">R &amp; T Summit Construction</div>

    <div class="contact contact-first">
      <div class="contact-name">Nolan Pritchett</div>
      <div class="contact-line">
        <svg viewBox="0 0 10 10"><path d="M2 0.5 L3.6 2.6 L2.7 3.6 Q3.8 5.9 6.4 7.3 L7.4 6.4 L9.5 8 L8.2 9.5 Q4.5 9.3 2 6.5 Q0.3 4.3 0.5 1.8 Z"/></svg>
        <span>512-804-2271</span>
      </div>
      <div class="contact-line">
        <svg viewBox="0 0 10 10"><path d="M0.5 1.8 H9.5 V2.6 L5 5.4 L0.5 2.6 Z M0.5 3.8 L5 6.6 L9.5 3.8 V8.4 H0.5 Z"/></svg>
        <span>nolan@rtsummitbuild.com</span>
      </div>
    </div>

    <div class="contact contact-second">
      <div class="contact-name">Curtis Hale</div>
      <div class="contact-line">
        <svg viewBox="0 0 10 10"><path d="M2 0.5 L3.6 2.6 L2.7 3.6 Q3.8 5.9 6.4 7.3 L7.4 6.4 L9.5 8 L8.2 9.5 Q4.5 9.3 2 6.5 Q0.3 4.3 0.5 1.8 Z"/></svg>
        <span>512-693-1804</span>
      </div>
      <div class="contact-line">
        <svg viewBox="0 0 10 10"><path d="M0.5 1.8 H9.5 V2.6 L5 5.4 L0.5 2.6 Z M0.5 3.8 L5 6.6 L9.5 3.8 V8.4 H0.5 Z"/></svg>
        <span>curtis@rtsummitbuild.com</span>
      </div>
    </div>
  </section>

  <section class="card card-back">
    <div class="company-name">R &amp; T Summit Construction</div>
  </section>
</div>
</body>
</html>
```